First Aid Kit needs packaging design

We're looking for packaging design for our new first aid kit product. We have the logo created for the product. Our brand name is Velmont Shield and our logo will be provided during the design process. We'll also provide photos (have high res files files for final design), and a template design to base off what we're looking for (packaging design template is .ai file). Logo file also attached (.psd & .png). We need to have the first aid kit contents listed on the back of the packaging (similar to the provided packaging template).

Color: We would like to see black, red, and white throughout the design (similar to provided design template)

The final design should communicate urgency, safety, and portability.

Final design should also include a FNSKU barcode (attached)

Below are more details that define the product.

Product Name:
Ultra-Portable & Small 100-Piece First Aid Kit w/ Exclusive Items, Light, Durable Nylon Case, Space Saving Design - A Must Have Survival Kit!

Product Attributes:
BASED ON CUSTOMER FEEDBACK, our newly designed ultra-lightweight and portable kit has been upgraded with BETTER and STRONGER emergency supplies. Stronger scissors and tweezers, more precise compass, sting relief pads, antibacterial ointment and more!
PRODUCED WITH THE HIGHEST QUALITY STANDARDS that only KLT Approved Facilities can meet.
LIGHTWEIGHT, DURABLE & COMPACT. Perfect for an emergency where a Velmont Shield is necessary to because seconds count!
The ULTIMATE First Aid Kit for Camping, Home, Road Trips, Office, Adventure, School, Workplace, Travel or Sports.

Product Description
Learn How This Ultra-Portable, Light And Rugged First-Aid Kit Can Give You And Your Family The Ultimate Peace Of Mind.
You need to act fast! Quick Action And A Velmont Shield Is Critical In Emergency Situations.

Stay Alert! Our Kit Has Been Redesigned And Bolstered Based On Your Feedback. Weighing Under 1lb. This Is The Lightest First Aid Kit In Its Class! If You Don't Know What To Do, No Problem; We've Included A First Aid Instruction Guide So You Can Administer Aid Correctly.

Take A Look Inside:

Antiseptic cleansing wipes (6 pcs)
Alcohol prep pad (10 pcs)
Butterfly closure strips (6 pcs)
Sterile Gauze Pad (3 pcs)
Extra large adhesive bandage (4 pc)
Adhesive bandages (25 pcs)
Antibacterial Ointment (4 pcs)
Knuckle adhesive bandage (3 pcs)
Fingertip adhesive bandage (3 pcs)
1 disposable cold compress
First aid tape (1 roll)
Cotton tip applicator (10 pcs)
Abdominal pad (1 pc)
Disposable vinyl gloves (2 pc)
Slim rescue howler whistle (1 pc)
Compass (1pc)
Moleskin blister relief (1 pc)
Triangular bandages (1 pc)
Disposable Emergency blanket (1 pc)
1 glow stick
Disposable raincoat (1 pc)
Scissors (1 pc)
PBT conforming bandage 5x3.6cm (1 roll)
CPR facemask (1 pc)
Metal tweezers (1 pc)
Razor Blade (1 pc)
Sewing Kit (1 pc)
Safety Pins (4 pc)
Sting Relief Pads (4 pc)

Let us know if there are any questions around this.

Thank you,

Orin

Target Market(s)

Health Care, First Aid, Sports & Outdoors, automotive safety, office safety

Industry/Entity Type

Health Care

Font styles to use
Sans Serif
Other font styles liked:
• similar to included box design frame/template

Colors
ec1f27
ffffff
000000

Requirements
Must have
• See Project Description
• Color: Black, red, and white
• Barcode: FNSKU Barcode attached
• Design on back needs to show included contents (similar to design template attached)
Nice to have
• See Project Description

```html
<!DOCTYPE html>
<html lang="en">
<head>
<meta charset="utf-8">
<title>Velmont Shield First Aid Kit – Packaging</title>
<link href="https://fonts.googleapis.com/css2?family=Oswald:wght@400;500;600&family=Montserrat:wght@500;700&family=Roboto+Condensed:wght@400&display=swap" rel="stylesheet">
<style>
  :root{
    --red:#ec1f27;
    --black:#1b1717;
    --ink:#000000;
    --white:#ffffff;
    --grey:#3a3535;
    --grey-light:#4a4545;
    --line:#8c8787;
    --placeholder:#f6d3d5;
    --stage:#f2f2f2;
  }
  *{box-sizing:border-box;margin:0;padding:0}
  html,body{width:1200px;height:711px;overflow:hidden;background:var(--stage)}
  .canvas{position:relative;width:1200px;height:711px}
  .sprite{position:absolute;width:0;height:0;overflow:hidden}

  .panel{position:absolute;top:45px;height:620px;background:var(--black);overflow:hidden;color:var(--white)}
  .side--front{left:20px;width:70px}
  .panel--front{left:90px;width:450px;border-left:1px solid #2e2929}
  .side--back{left:560px;width:70px}
  .panel--back{left:630px;width:550px;border-left:1px solid #2e2929}

  .case-view{position:absolute;left:0;top:0;width:100%;height:120px;
    background:linear-gradient(180deg,#2a2626 0%,#2a2626 45%,#c9161d 46%,var(--red) 100%)}

  /* narrow side panel */
  .side-body{position:absolute;top:120px;left:0;width:100%;height:500px;display:flex;flex-direction:column;align-items:center;padding-top:12px}
  .side-dot{width:34px;height:34px;border-radius:50%;background:var(--white)}
  .side-pieces{margin-top:10px;writing-mode:vertical-rl;font-family:"Oswald",sans-serif;font-weight:600;color:var(--red);line-height:1;display:flex;align-items:center}
  .side-pieces .num{font-size:40px}
  .side-pieces .lbl{font-size:18px;font-weight:500}
  .side-ideal{margin-top:10px;writing-mode:vertical-rl;font-family:"Oswald",sans-serif;font-size:11.5px;line-height:1.25;text-align:center}
  .side-list{margin-top:10px;width:48px;list-style:none;border-top:1px solid #6b6565}
  .side-list li{height:31px;border-bottom:1px solid #6b6565;display:flex;align-items:center;gap:4px;padding-left:3px}
  .side-list svg{width:11px;height:11px;color:var(--white);flex:none}
  .side-list .ph{width:11px;height:11px;background:var(--placeholder);flex:none}
  .side-list span.lbl{writing-mode:vertical-rl;font-family:"Oswald",sans-serif;font-size:9px;line-height:1}

  /* activity column */
  .pieces-column{position:absolute;top:120px;height:500px;background:var(--red);
    display:flex;flex-direction:column;align-items:center;padding-top:22px}
  .panel--front .pieces-column{left:340px;width:110px}
  .panel--back .pieces-column{left:0;width:130px}
  .pieces-count{font-family:"Oswald",sans-serif;font-weight:600;font-size:60px;line-height:.95}
  .pieces-label{font-family:"Oswald",sans-serif;font-weight:500;font-size:27px;line-height:1;letter-spacing:1px}
  .activity-note{margin-top:10px;padding-top:8px;border-top:1px solid var(--white);width:86%;
    text-align:center;font-family:"Oswald",sans-serif;font-size:14px;line-height:1.25}
  .activity-grid{margin-top:14px;display:grid;grid-template-columns:repeat(2,40px);gap:8px}
  .activity-icon{width:40px;height:40px;background:var(--white);display:flex;align-items:center;justify-content:center;color:var(--red)}
  .activity-icon svg{width:28px;height:28px}
  .activity-icon--ph{background:var(--placeholder)}
  .more-note{margin-top:auto;margin-bottom:24px;font-family:"Oswald",sans-serif;font-size:12px}

  /* brand */
  .brand{position:absolute;display:flex;flex-direction:column;align-items:center;gap:10px}
  .brand-dot{width:64px;height:64px;border-radius:50%;background:var(--white)}
  .brand-name{font-family:"Montserrat",sans-serif;font-weight:700;font-size:22px;color:var(--white)}
  .panel--front .brand{left:0;width:340px;top:210px}
  .panel--back .brand{left:135px;width:170px;top:140px}
  .panel--back .brand-dot{width:50px;height:50px}
  .panel--back .brand-name{font-size:16px}

  .red-tab{position:absolute;left:110px;top:120px;width:125px;height:44px;background:var(--red)}

  .tagline{position:absolute;left:0;width:340px;top:370px;text-align:center;
    font-family:"Montserrat",sans-serif;font-weight:500;font-size:12.5px;line-height:1.6;letter-spacing:.8px}
  .survival-banner{position:absolute;left:0;top:545px;width:340px;height:50px;background:var(--red);
    font-family:"Oswald",sans-serif;font-weight:500;font-size:26px;line-height:50px;text-align:center;letter-spacing:.5px}

  /* back */
  .tagline-box{position:absolute;left:305px;top:140px;width:245px;height:92px;background:var(--red);
    padding:12px 12px;font-family:"Montserrat",sans-serif;font-weight:500;font-size:12px;line-height:1.45;letter-spacing:.5px}
  .contents-grid{position:absolute;left:140px;top:268px;display:grid;grid-template-columns:repeat(4,46px);
    grid-template-rows:repeat(4,46px);column-gap:6px;row-gap:30px}
  .contents-icon{border:1.5px solid var(--line);background:var(--grey);display:flex;align-items:center;justify-content:center;color:var(--white)}
  .contents-icon svg{width:30px;height:30px;fill:none;stroke:currentColor;stroke-width:1.4;stroke-linecap:round;stroke-linejoin:round}
  .kit-list{position:absolute;left:350px;top:248px;width:192px}
  .kit-list h2{font-family:"Oswald",sans-serif;font-weight:400;font-size:17px;letter-spacing:.5px;
    border-bottom:1px solid var(--white);padding-bottom:2px;margin-bottom:3px}
  .kit-table{width:100%;border-collapse:collapse;font-family:"Roboto Condensed",sans-serif;font-size:6.6px;color:#e6e6e6}
  .kit-table tr{height:11px}
  .kit-table tr:nth-child(odd){background:var(--grey-light)}
  .kit-table td{padding:0 3px;white-space:nowrap}
  .kit-table td.qty{text-align:right}
</style>
</head>
<body>
<svg class="sprite" aria-hidden="true">
  <symbol id="ic-tent" viewBox="0 0 24 24"><path fill="currentColor" fill-rule="evenodd" d="M2 20 L12 4 L22 20 Z M12 11 L9 20 L15 20 Z"/></symbol>
  <symbol id="ic-car" viewBox="0 0 24 24"><path fill="currentColor" fill-rule="evenodd" d="M3 15 L6 8 H18 L21 15 V19 H3 Z M7.5 9.5 H16.5 L18 13.5 H6 Z"/><circle cx="7" cy="19.5" r="2" fill="currentColor"/><circle cx="17" cy="19.5" r="2" fill="currentColor"/></symbol>
  <symbol id="ic-house" viewBox="0 0 24 24"><path fill="currentColor" fill-rule="evenodd" d="M2 12 L12 3 L22 12 H19 V21 H5 V12 Z M10 14 H14 V21 H10 Z"/></symbol>
  <symbol id="ic-case" viewBox="0 0 24 24"><path fill="currentColor" d="M3 8 H21 V20 H3 Z M9 8 V4.5 H15 V8 H13.5 V6 H10.5 V8 Z"/></symbol>
</svg>
<main class="canvas">

  <!-- Front: side panel -->
  <section class="panel side--front">
    <div class="case-view" role="img" aria-label="Photo of the red nylon kit case"></div>
    <div class="side-body">
      <span class="side-dot"></span>
      <div class="side-pieces"><span class="num">100</span><span class="lbl">PIECES</span></div>
      <p class="side-ideal">IDEAL FOR<br>ALL ACTIVITES</p>
      <ul class="side-list">
        <li><svg><use href="#ic-tent"/></svg><span class="lbl">Camping</span></li>
        <li><span class="ph" role="img" aria-label="Hiker icon"></span><span class="lbl">Outdoors</span></li>
        <li><span class="ph" role="img" aria-label="Runner icon"></span><span class="lbl">Sports</span></li>
        <li><svg><use href="#ic-car"/></svg><span class="lbl">Vehicles</span></li>
        <li><span class="ph" role="img" aria-label="Office worker icon"></span><span class="lbl">Office</span></li>
        <li><svg><use href="#ic-house"/></svg><span class="lbl">Home</span></li>
        <li><span class="ph" role="img" aria-label="Traveller icon"></span><span class="lbl">Travel</span></li>
        <li><svg><use href="#ic-case"/></svg><span class="lbl">General</span></li>
      </ul>
    </div>
  </section>

  <!-- Front face -->
  <section class="panel panel--front">
    <div class="case-view" role="img" aria-label="Photo of the red nylon kit case with black carry handles"></div>
    <div class="red-tab"></div>
    <div class="brand"><span class="brand-dot"></span><span class="brand-name">Velmont Shield</span></div>
    <p class="tagline">Ultra-Portable &amp; Small<br>100-Piece First Aid Kit with Exclusive Items<br>Durable Nylon Case<br>Light &amp; Space Saving Design</p>
    <div class="survival-banner">A MUST HAVE SURVIVAL KIT!</div>
    <aside class="pieces-column">
      <div class="pieces-count">100</div>
      <div class="pieces-label">PIECES</div>
      <p class="activity-note">IDEAL FOR<br>ALL ACTIVITES</p>
      <div class="activity-grid">
        <span class="activity-icon"><svg><use href="#ic-tent"/></svg></span>
        <span class="activity-icon activity-icon--ph" role="img" aria-label="Hiker icon"></span>
        <span class="activity-icon activity-icon--ph" role="img" aria-label="Runner icon"></span>
        <span class="activity-icon"><svg><use href="#ic-car"/></svg></span>
        <span class="activity-icon activity-icon--ph" role="img" aria-label="Office worker icon"></span>
        <span class="activity-icon"><svg><use href="#ic-house"/></svg></span>
        <span class="activity-icon activity-icon--ph" role="img" aria-label="Traveller icon"></span>
        <span class="activity-icon"><svg><use href="#ic-case"/></svg></span>
      </div>
      <p class="more-note">AND SO MUCH MORE</p>
    </aside>
  </section>

  <!-- Back: side panel -->
  <section class="panel side--back">
    <div class="case-view" role="img" aria-label="Photo of the red nylon kit case"></div>
    <div class="side-body">
      <span class="side-dot"></span>
      <div class="side-pieces"><span class="num">100</span><span class="lbl">PIECES</span></div>
      <p class="side-ideal">IDEAL FOR<br>ALL ACTIVITES</p>
      <ul class="side-list">
        <li><svg><use href="#ic-tent"/></svg><span class="lbl">Camping</span></li>
        <li><span class="ph" role="img" aria-label="Hiker icon"></span><span class="lbl">Outdoors</span></li>
        <li><span class="ph" role="img" aria-label="Runner icon"></span><span class="lbl">Sports</span></li>
        <li><svg><use href="#ic-car"/></svg><span class="lbl">Vehicles</span></li>
        <li><span class="ph" role="img" aria-label="Office worker icon"></span><span class="lbl">Office</span></li>
        <li><svg><use href="#ic-house"/></svg><span class="lbl">Home</span></li>
        <li><span class="ph" role="img" aria-label="Traveller icon"></span><span class="lbl">Travel</span></li>
        <li><svg><use href="#ic-case"/></svg><span class="lbl">General</span></li>
      </ul>
    </div>
  </section>

  <!-- Back face -->
  <section class="panel panel--back">
    <div class="case-view" role="img" aria-label="Photo of the red nylon kit case with black carry handles"></div>
    <aside class="pieces-column">
      <div class="pieces-count">100</div>
      <div class="pieces-label">PIECES</div>
      <p class="activity-note">IDEAL FOR<br>ALL ACTIVITES</p>
      <div class="activity-grid">
        <span class="activity-icon"><svg><use href="#ic-tent"/></svg></span>
        <span class="activity-icon activity-icon--ph" role="img" aria-label="Hiker icon"></span>
        <span class="activity-icon activity-icon--ph" role="img" aria-label="Runner icon"></span>
        <span class="activity-icon"><svg><use href="#ic-car"/></svg></span>
        <span class="activity-icon activity-icon--ph" role="img" aria-label="Office worker icon"></span>
        <span class="activity-icon"><svg><use href="#ic-house"/></svg></span>
        <span class="activity-icon activity-icon--ph" role="img" aria-label="Traveller icon"></span>
        <span class="activity-icon"><svg><use href="#ic-case"/></svg></span>
      </div>
      <p class="more-note">AND SO MUCH MORE</p>
    </aside>
    <div class="brand"><span class="brand-dot"></span><span class="brand-name">Velmont Shield</span></div>
    <p class="tagline-box">Ultra-Portable &amp; Small<br>100-Piece First Aid Kit<br>Durable Nylon Case<br>Light &amp; Space Saving Design</p>

    <div class="contents-grid">
      <span class="contents-icon" aria-label="Whistle"><svg viewBox="0 0 24 24"><path d="M3 9 H16 A5 5 0 1 1 11 15 H7 L3 12 Z"/><path d="M12 9 V6 H15"/></svg></span>
      <span class="contents-icon" aria-label="Tape roll"><svg viewBox="0 0 24 24"><ellipse cx="9" cy="12" rx="5" ry="8"/><ellipse cx="9" cy="12" rx="2" ry="3.5"/><path d="M9 4 H18 V20 H9"/></svg></span>
      <span class="contents-icon" aria-label="Emergency blanket"><svg viewBox="0 0 24 24"><rect x="4" y="4" width="16" height="16" rx="2"/><path d="M4 16 H20"/></svg></span>
      <span class="contents-icon" aria-label="Compass"><svg viewBox="0 0 24 24"><circle cx="12" cy="12" r="9"/><path d="M12 5 L14 12 L12 19 L10 12 Z"/><path d="M5 12 L12 10 L19 12 L12 14 Z"/></svg></span>
      <span class="contents-icon" aria-label="Glow stick"><svg viewBox="0 0 24 24"><path d="M7 18 L17 6"/><path d="M4 9 L7 10 M9 4 L10 7 M17 20 L16 17 M20 15 L17 14"/></svg></span>
      <span class="contents-icon" aria-label="CPR facemask"><svg viewBox="0 0 24 24"><path d="M5 9 Q12 5 19 9 L18 15 Q12 19 6 15 Z"/><path d="M2 8 L5 10 M22 8 L19 10 M2 16 L6 14 M22 16 L18 14"/><path d="M12 10 V14 M10 12 H14"/></svg></span>
      <span class="contents-icon" aria-label="Gloves"><svg viewBox="0 0 24 24"><path d="M7 21 V11 L5 8 M7 11 V4 M10 11 V3 M13 11 V4 M16 12 V6 M16 12 L19 9 M7 21 H15 L16 12"/></svg></span>
      <span class="contents-icon" aria-label="Poncho"><svg viewBox="0 0 24 24"><path d="M9 4 H15 L21 10 L19 20 H5 L3 10 Z"/><path d="M9 4 Q12 8 15 4"/></svg></span>
      <span class="contents-icon" aria-label="Safety pin"><svg viewBox="0 0 24 24"><path d="M5 19 L17 7"/><path d="M6 20 L18 8 A2.5 2.5 0 0 0 15 5"/><circle cx="5" cy="19" r="1.5"/></svg></span>
      <span class="contents-icon" aria-label="Razor blade"><svg viewBox="0 0 24 24"><rect x="3" y="8" width="18" height="8" rx="1"/><path d="M8 12 H16"/><circle cx="8" cy="12" r="1.5"/><circle cx="16" cy="12" r="1.5"/></svg></span>
      <span class="contents-icon" aria-label="Tweezers"><svg viewBox="0 0 24 24"><path d="M4 4 L19 19 M4 4 L20 17"/></svg></span>
      <span class="contents-icon" aria-label="Bandage roll"><svg viewBox="0 0 24 24"><circle cx="12" cy="12" r="9"/><circle cx="12" cy="12" r="6"/><circle cx="12" cy="12" r="3"/></svg></span>
      <span class="contents-icon" aria-label="Adhesive bandage"><svg viewBox="0 0 24 24"><rect x="2" y="8" width="20" height="8" rx="4" transform="rotate(-35 12 12)"/><rect x="9" y="9" width="6" height="6" transform="rotate(-35 12 12)"/></svg></span>
      <span class="contents-icon" aria-label="Cotton swab"><svg viewBox="0 0 24 24"><path d="M7 7 L17 17"/><ellipse cx="5.5" cy="5.5" rx="2.5" ry="1.6" transform="rotate(45 5.5 5.5)"/><ellipse cx="18.5" cy="18.5" rx="2.5" ry="1.6" transform="rotate(45 18.5 18.5)"/></svg></span>
      <span class="contents-icon" aria-label="Sewing kit"><svg viewBox="0 0 24 24"><path d="M6 20 L17 4"/><ellipse cx="16.3" cy="5" rx=".8" ry="1.6" transform="rotate(35 16.3 5)"/><path d="M16 6 Q22 12 16 20"/></svg></span>
      <span class="contents-icon" aria-label="Ointment bottles"><svg viewBox="0 0 24 24"><rect x="3" y="9" width="8" height="12" rx="1"/><path d="M5 9 V6 H9 V9"/><rect x="13" y="11" width="8" height="10" rx="1"/><path d="M15 11 V8 H19 V11"/></svg></span>
    </div>

    <div class="kit-list">
      <h2>WHATS IN THE KIT</h2>
      <table class="kit-table">
        <tr><td>Abdominal bandage</td><td>5"x9"</td><td class="qty">1</td></tr>
        <tr><td>Adhesive bandage, extra large</td><td>Extra Large Size</td><td class="qty">4</td></tr>
        <tr><td>Adhesive bandage</td><td>For Fingertips</td><td class="qty">3</td></tr>
        <tr><td>Adhesive bandage</td><td>For Knuckles</td><td class="qty">3</td></tr>
        <tr><td>Adhesive bandage</td><td>Standard Size</td><td class="qty">25</td></tr>
        <tr><td>Alcohol prep pads</td><td></td><td class="qty">10</td></tr>
        <tr><td>Antibacterial ointment</td><td></td><td class="qty">4</td></tr>
        <tr><td>Antiseptic wipes</td><td></td><td class="qty">6</td></tr>
        <tr><td>Butterfly closure strips</td><td></td><td class="qty">6</td></tr>
        <tr><td>Cold compress, disposable</td><td>100g</td><td class="qty">1</td></tr>
        <tr><td>Compass</td><td></td><td class="qty">1</td></tr>
        <tr><td>Cotton tip applicators</td><td></td><td class="qty">10</td></tr>
        <tr><td>CPR facemask</td><td></td><td class="qty">1</td></tr>
        <tr><td>Elastic conforming bandage</td><td>5cm x 3.6m</td><td class="qty">1</td></tr>
        <tr><td>Emergency blanket</td><td>210 x 130cm</td><td class="qty">1</td></tr>
        <tr><td>First aid tape</td><td></td><td class="qty">1</td></tr>
        <tr><td>Gauze pad, sterile</td><td></td><td class="qty">3</td></tr>
        <tr><td>Glow stick</td><td></td><td class="qty">1</td></tr>
        <tr><td>Metal tweezer</td><td></td><td class="qty">1</td></tr>
        <tr><td>Moleskin blister relief pad</td><td></td><td class="qty">1</td></tr>
        <tr><td>Poncho, disposable</td><td></td><td class="qty">1</td></tr>
        <tr><td>Razor blade</td><td></td><td class="qty">1</td></tr>
        <tr><td>Rescue whistle</td><td></td><td class="qty">1</td></tr>
        <tr><td>Safety pins</td><td></td><td class="qty">4</td></tr>
        <tr><td>Scissors</td><td></td><td class="qty">1</td></tr>
        <tr><td>Sewing kit</td><td></td><td class="qty">1</td></tr>
        <tr><td>Sting relief pads</td><td></td><td class="qty">4</td></tr>
        <tr><td>Triangular bandage</td><td>96 x 96 x 136cm</td><td class="qty">1</td></tr>
        <tr><td>Vinyl gloves, disposable</td><td>Large size</td><td class="qty">2</td></tr>
      </table>
    </div>
  </section>

</main>
</body>
</html>
```